PROPERTY MANAGEMENT AND REAL ESTATE

Target Market(s)

real estate owners and investors

Industry/Entity Type

Real Estate

Contact Information for Business Card

BRIGHT HARBOR PROPERTY MANAGEMENT GROUP, LLC
287 West Marlow Parkway
Suite 240
Hallandale Beach, FL 33009

```html
<!DOCTYPE html>
<html lang="en">
<head>
<meta charset="utf-8">
<title>Bright Harbor Property Management Group – Business Card</title>
<link rel="stylesheet" href="https://fonts.googleapis.com/css2?family=Cinzel:wght@400;600&family=Josefin+Sans:wght@300;400&display=swap">
<style>
  :root {
    --backdrop: #8d8f8e;
    --paper: #fbfbf9;
    --brand-red: #b01e24;
    --deep-red: #7a1418;
    --near-black: #1b0d0d;
    --ink: #2f2f2f;
    --ink-soft: #555555;
    --cream: #f3ebe6;
    --white: #ffffff;
  }
  * { margin: 0; padding: 0; box-sizing: border-box; }
  html, body {
    width: 1200px; height: 809px; overflow: hidden;
    background: var(--backdrop);
  }
  .canvas { position: relative; width: 1200px; height: 809px; }

  .card {
    position: absolute; top: 250px;
    width: 540px; height: 309px;
    background: var(--paper);
    box-shadow: 0 6px 18px rgba(0,0,0,.28);
    overflow: hidden;
  }
  .card--front { left: 40px; }
  .card--back  { left: 620px; }

  /* Front */
  .front__top-band {
    position: absolute; left: 0; top: 0; width: 100%; height: 28px;
    background: linear-gradient(90deg, var(--near-black) 0%, var(--deep-red) 45%, var(--near-black) 100%);
  }
  .brand-mark {
    position: absolute; border-radius: 50%;
    background: var(--brand-red);
  }
  .front__mark { left: 34px; top: 62px; width: 150px; height: 150px; }
  .front__name {
    position: absolute; left: 204px; top: 100px; width: 320px;
    font-family: "Josefin Sans", sans-serif; font-weight: 300;
    font-size: 22px; line-height: 32px; letter-spacing: .3px;
    color: var(--ink); text-transform: uppercase;
  }
  .front__tagline-band {
    position: absolute; left: 0; bottom: 0; width: 100%; height: 58px;
    background: linear-gradient(90deg, var(--near-black) 0%, var(--deep-red) 50%, var(--brand-red) 100%);
    display: flex; align-items: center; padding-left: 30px;
  }
  .front__tagline {
    font-family: "Cinzel", serif; font-size: 17px; letter-spacing: 1px;
    color: var(--cream);
  }

  /* Back */
  .back__brand {
    position: absolute; left: 22px; top: 30px; width: 230px;
  }
  .back__mark { position: static; display: block; width: 82px; height: 82px; margin-bottom: 14px; }
  .back__name {
    font-family: "Josefin Sans", sans-serif; font-weight: 300;
    font-size: 13px; line-height: 18px; letter-spacing: .3px;
    color: var(--ink-soft); text-transform: uppercase;
  }
  .back__panel {
    position: absolute; left: 262px; top: 8px; right: 8px; bottom: 8px;
    background: linear-gradient(200deg, var(--near-black) 0%, var(--deep-red) 35%, var(--brand-red) 70%, #c2262b 100%);
    padding: 22px 16px 0 18px;
    color: var(--white); font-family: "Cinzel", serif;
  }
  .contact__person { text-align: right; margin-bottom: 20px; }
  .contact__name { font-size: 27px; font-weight: 600; letter-spacing: 1px; line-height: 32px; }
  .contact__title { font-size: 17px; line-height: 21px; letter-spacing: 1px; }
  .contact__list { list-style: none; }
  .contact__item {
    display: flex; align-items: flex-start; gap: 10px;
    font-size: 12px; line-height: 16px; margin-bottom: 11px; letter-spacing: .2px;
  }
  .contact__icon { flex: 0 0 20px; width: 20px; height: 20px; }
</style>
</head>
<body>
<main class="canvas">

  <section class="card card--front" aria-label="Business card front">
    <div class="front__top-band"></div>
    <span class="brand-mark front__mark" aria-hidden="true"></span>
    <h1 class="front__name">Bright Harbor Property<br>Management Group, LLC</h1>
    <div class="front__tagline-band">
      <p class="front__tagline">REAL ESTATE OWNERS AND INVESTORS</p>
    </div>
  </section>

  <section class="card card--back" aria-label="Business card back">
    <div class="back__brand">
      <span class="brand-mark back__mark" aria-hidden="true"></span>
      <p class="back__name">Bright Harbor Property<br>Management Group, LLC</p>
    </div>

    <div class="back__panel">
      <div class="contact__person">
        <p class="contact__name">DANIEL REYES</p>
        <p class="contact__title">MANAGING<br>DIRECTOR</p>
      </div>
      <ul class="contact__list">
        <li class="contact__item">
          <svg class="contact__icon" viewBox="0 0 24 24" aria-hidden="true">
            <path fill="#fff" d="M6.6 10.8a15.1 15.1 0 0 0 6.6 6.6l2.2-2.2a1 1 0 0 1 1-.25 11.4 11.4 0 0 0 3.6.57 1 1 0 0 1 1 1V20a1 1 0 0 1-1 1A17 17 0 0 1 3 4a1 1 0 0 1 1-1h3.5a1 1 0 0 1 1 1c0 1.25.2 2.450.57 3.57a1 1 0 0 1-.25 1z"/>
          </svg>
          <span>(954) 555-0142</span>
        </li>
        <li class="contact__item">
          <svg class="contact__icon" viewBox="0 0 24 24" aria-hidden="true">
            <path fill="none" stroke="#fff" stroke-width="2" d="M12 22s-7-7.2-7-12a7 7 0 0 1 14 0c0 4.8-7 12-7 12z"/>
            <circle cx="12" cy="10" r="2.6" fill="#fff"/>
          </svg>
          <span>287 WEST MARLOW PARKWAY<br>SUITE 240<br>HALLANDALE BEACH<br>FL 33009</span>
        </li>
        <li class="contact__item">
          <svg class="contact__icon" viewBox="0 0 24 24" aria-hidden="true">
            <rect x="2" y="2" width="20" height="20" rx="3" fill="#fff"/>
          </svg>
          <span>WWW.BRIGHTHARBORPM.COM</span>
        </li>
      </ul>
    </div>
  </section>

</main>
</body>
</html>
```